Web, logo, and business card Design

We are opening a cocktail/Cork Den which serves tapas. It's outdoors surrounded by an old heritage listed building 'Elder Colonial Lodge' in the midst of a park. The bar will be full of ambience with an industrial feel but also fun, young and fresh, not old and stuffy. Fairy lights, old barrels, big colourful couches and high tables will mostly make up the decor along with candles, plants and building uplighting. We will offer 3 private rooms for small functions, the only indoor areas available. Fireplaces and heaters will be everywhere during an Aussie winter and umbrellas for those hot days. The establishment is named 'Cork Den'. We are after a logo design, web design and business card design to suit the style of our establishment.

Target Market(s)

Young professionals, couples and groups

Contact Information for Business Card

Name: Cork Den
Address: Elder Colonial Lodge
Wendlow Reserve
Wendlow NSW 2163 (enter the park from Quarrel St)

1km from the new Wendlow Arena and Wendlow Station

Website: corkdenhaven.example.au
Email: info@corkdenhaven.example
facebook: Cork Den Haven
Instagram: Cork Den Haven

Logo Text

Cork Den

Coding

Coded - Design and coding required

Number of Pages Required

1 page

Colors

Designer to choose colors to be used in the design.

Requirements
Must have
• Must have a home page and a click through to food Menu, drink menu (which we are still working on)
• Must be able to enquire and send emails easily from website.
• I must be able to update myself easily should anything change
• There's a basic temporary site available which you will be replacing, feel free to have a look.
• Looking for fun, sexy, fresh, ambience. The venue is a historic one.
Nice to have
• Map, reservations tab, a little info about Elder Colonial lodge. There's some already on the current site which you can use. Music perhaps?

```html
<!DOCTYPE html>
<html lang="en">
<head>
<meta charset="utf-8">
<title>Cork Den — Wine, Cocktails and Tapas</title>
<link href="https://fonts.googleapis.com/css2?family=Oswald:wght@300;400;500&family=Open+Sans:wght@400;600&family=Montserrat:wght@400;500;600&display=swap" rel="stylesheet">
<style>
:root{
  --purple:#8d1f95;
  --purple-deep:#5b168d;
  --magenta:#c8348f;
  --pink:#e055d4;
  --ink:#0b0b0b;
  --white:#ffffff;
  --footer-top:#7b22ad;
  --footer-bottom:#54168a;
  --head:'Oswald',sans-serif;
  --body:'Open Sans',sans-serif;
  --ui:'Montserrat',sans-serif;
}
*{box-sizing:border-box;margin:0;padding:0}
html,body{width:1200px;height:3285px;overflow:hidden;background:#111}
body{position:relative;font-family:var(--body);color:var(--white)}
.abs{position:absolute}

/* hero */
.hero{position:absolute;left:0;top:0;width:1200px;height:715px;
  background:
    radial-gradient(ellipse 260px 180px at 220px 180px,rgba(170,110,70,.55),transparent 70%),
    radial-gradient(ellipse 300px 200px at 900px 600px,rgba(120,60,40,.5),transparent 70%),
    radial-gradient(ellipse 240px 160px at 560px 420px,rgba(150,100,60,.45),transparent 70%),
    radial-gradient(ellipse at 30% 40%,#6b4a33 0%,#3a2619 45%,#1a120d 100%)}
.hero-shade{position:absolute;inset:0;background:linear-gradient(90deg,rgba(0,0,0,.45),rgba(0,0,0,.15) 60%,rgba(0,0,0,.35))}
.nav-bar{position:absolute;left:0;top:58px;width:1200px;height:60px;background:rgba(0,0,0,.45)}
.nav a{position:absolute;top:80px;font-family:var(--head);font-weight:400;font-size:15px;color:var(--white);text-decoration:none;letter-spacing:.2px;white-space:nowrap}
.nav a.active{color:var(--pink)}
.brand{position:absolute;left:526px;top:20px;width:144px;height:144px;border-radius:50%;background:#0d0d0d;border:3px solid var(--purple);display:flex;align-items:center;justify-content:center;gap:8px}
.brand-dot{width:10px;height:10px;border-radius:50%;background:var(--pink)}
.brand-name{font-family:var(--head);font-weight:400;font-size:28px;color:var(--white)}
.hero-kicker{position:absolute;left:155px;top:288px;font-family:var(--head);font-weight:300;font-size:38px;letter-spacing:1px}
.hero-title{position:absolute;left:155px;top:342px;font-family:var(--head);font-weight:300;font-size:52px;letter-spacing:1px;line-height:1.2}
.btn{position:absolute;display:flex;align-items:center;justify-content:center;font-family:var(--ui);font-weight:600;color:var(--white);text-decoration:none}
.btn-menu{left:153px;top:436px;width:176px;height:41px;background:var(--purple);font-size:15px}
.enquiry{position:absolute;left:758px;top:201px;width:337px;height:353px;border-radius:6px;
  background:linear-gradient(180deg,#b12c9f 0%,#8a1f8e 100%);box-shadow:0 4px 14px rgba(0,0,0,.4)}
.enquiry h2{position:absolute;left:0;width:100%;top:20px;text-align:center;font-family:var(--head);font-weight:400;font-size:30px}
.field{position:absolute;left:35px;width:271px;height:31px;border:1px solid rgba(255,255,255,.85);font-family:var(--body);font-size:12px;padding:6px 12px}
.field.tall{height:81px}
.enquiry .submit{left:35px;top:287px;width:271px;height:35px;background:#000;font-size:14px}
.dots{position:absolute;left:542px;top:621px;display:flex;gap:6px;align-items:center}
.dots span{width:8px;height:8px;border-radius:50%;background:#888}
.dots span.on{background:#fff}
.dots i{width:20px;height:20px;border-radius:50%;background:#fff;display:block}

/* features */
.features{position:absolute;left:0;top:712px;width:1200px;height:403px;
  background:linear-gradient(90deg,#2a2522,#3a332e 50%,#2b2623)}
.feature-label{position:absolute;font-family:var(--head);font-weight:300;font-size:30px;text-align:center;width:300px}

/* about */
.about{position:absolute;left:0;top:1115px;width:1200px;height:537px;
  background:
    radial-gradient(ellipse 180px 120px at 130px 150px,rgba(220,120,40,.7),transparent 70%),
    radial-gradient(ellipse 200px 130px at 330px 240px,rgba(230,150,50,.65),transparent 70%),
    radial-gradient(ellipse 220px 140px at 300px 420px,rgba(170,70,30,.6),transparent 70%),
    linear-gradient(135deg,#1d2d66 0%,#4a2a1e 40%,#6a3a1e 60%,#2a1a10 100%)}
.about h2{position:absolute;left:661px;width:400px;top:135px;text-align:center;font-family:var(--head);font-weight:300;font-size:40px}
.about p{position:absolute;left:655px;width:412px;top:210px;text-align:center;font-size:14.5px;line-height:22px}
.btn-more{left:786px;top:355px;width:154px;height:41px;border-radius:21px;background:#000;font-size:14px}

/* gallery */
.gallery-band{position:absolute;left:0;top:1652px;width:1200px;height:113px;background:#000}
.gallery-band h2{position:absolute;left:0;width:100%;top:30px;text-align:center;font-family:var(--head);font-weight:300;font-size:40px}
.tile{position:absolute;top:1765px;width:300px;height:245px}

/* reservations */
.reserve{position:absolute;left:0;top:2010px;width:1200px;height:486px;
  background:
    radial-gradient(ellipse 260px 120px at 200px 420px,rgba(120,80,50,.5),transparent 70%),
    radial-gradient(ellipse 280px 120px at 950px 430px,rgba(110,90,50,.5),transparent 70%),
    radial-gradient(ellipse at 50% 60%,#4a3a2c 0%,#2a221c 55%,#171310 100%)}
.reserve h2{position:absolute;left:0;width:100%;top:108px;text-align:center;font-family:var(--head);font-weight:300;font-size:40px}
.reserve p{position:absolute;left:200px;width:800px;top:172px;text-align:center;font-size:14.5px;line-height:24px;color:#e8e8e8}
.btn-book{left:519px;top:241px;width:158px;height:44px;border-radius:22px;background:var(--purple);font-size:15px}
.reserve h3{position:absolute;left:0;width:100%;top:325px;text-align:center;font-family:var(--head);font-weight:300;font-size:28px}
.hours{position:absolute;left:0;width:100%;top:380px;text-align:center;font-size:16px}

.map{position:absolute;left:0;top:2496px;width:1200px;height:421px;
  background:linear-gradient(90deg,#f2f2f2 0%,#e6e6e6 30%,#cfcfcf 60%,#bdbdbd 100%)}

/* footer */
.footer{position:absolute;left:0;top:2917px;width:1200px;height:368px;background:linear-gradient(180deg,var(--footer-top),var(--footer-bottom))}
.col{position:absolute;top:64px;font-family:var(--ui)}
.col h4{font-weight:500;font-size:16px;margin-bottom:18px}
.col li{list-style:none;font-size:12.5px;font-weight:500;line-height:26px;text-transform:uppercase;letter-spacing:.4px;white-space:nowrap}
.offer-form{position:absolute;left:773px;top:105px;width:300px;height:36px;border-radius:18px;background:#fff;display:flex;align-items:center;padding:0 6px 0 22px;justify-content:space-between}
.offer-form span{font-family:var(--ui);font-size:12px;color:#777}
.offer-form b{background:#000;color:#fff;font-family:var(--ui);font-weight:500;font-size:13px;border-radius:14px;padding:6px 22px}
.footer-rule{position:absolute;left:115px;top:304px;width:970px;height:1px;background:rgba(255,255,255,.3)}
.copyright{position:absolute;left:0;width:100%;top:328px;text-align:center;font-family:var(--ui);font-size:11px;color:rgba(255,255,255,.6)}
</style>
</head>
<body>

<header class="hero">
  <div class="hero-shade" role="img" aria-label="Tapas platters and wine glasses on a dark table"></div>
  <div class="nav-bar"></div>
  <nav class="nav">
    <a class="active" style="left:160px">HOME</a>
    <a style="left:228px">ABOUT US</a>
    <a style="left:322px">FOOD</a>
    <a style="left:386px">DRINK</a>
    <a style="left:455px">MAP</a>
    <a style="left:694px">RESERVATIONS</a>
    <a style="left:812px">ELDER COLONIAL LODGE</a>
    <a style="left:990px">CONTACT US</a>
  </nav>
  <div class="brand">
    <span class="brand-dot"></span><span class="brand-name">CORK DEN</span>
  </div>

  <div class="hero-kicker">WELCOME TO CORK DEN</div>
  <h1 class="hero-title">WINE, COCKTAILS AND TAPAS</h1>
  <a class="btn btn-menu">VIEW MENU</a>

  <form class="enquiry">
    <h2>ENQUIRIES</h2>
    <div class="field" style="top:73px">Name</div>
    <div class="field" style="top:112px">Email address</div>
    <div class="field" style="top:154px">Phone</div>
    <div class="field tall" style="top:193px">Message</div>
    <a class="btn submit">SUBMIT</a>
  </form>

  <div class="dots">
    <i></i><span class="on"></span><span></span><span></span><span></span><i></i>
  </div>
</header>

<section class="features">
  <svg class="abs" style="left:0;top:-30px" width="1200" height="60" viewBox="0 0 1200 60">
    <path d="M0 48 Q600 -10 1200 48" fill="none" stroke="#bdbdbd" stroke-width="5"/>
  </svg>
  <svg class="abs" style="left:0;top:0" width="1200" height="403" viewBox="0 0 1200 403">
    <defs>
      <radialGradient id="foodTone" cx="50%" cy="50%" r="60%">
        <stop offset="0" stop-color="#7a4526"/><stop offset="1" stop-color="#241712"/>
      </radialGradient>
      <radialGradient id="drinkTone" cx="50%" cy="50%" r="60%">
        <stop offset="0" stop-color="#7a2f2c"/><stop offset="1" stop-color="#231515"/>
      </radialGradient>
    </defs>
    <ellipse cx="355" cy="179" rx="237" ry="138" fill="url(#foodTone)" stroke="#d24bc6" stroke-width="3" role="img" aria-label="Plate of tapas"/>
    <ellipse cx="845" cy="179" rx="237" ry="138" fill="url(#drinkTone)" stroke="#d24bc6" stroke-width="3" role="img" aria-label="Glasses of red wine being raised"/>
  </svg>
  <div class="feature-label" style="left:205px;top:157px">OUR FOOD</div>
  <div class="feature-label" style="left:695px;top:157px">WINE &amp; DRINK</div>
</section>

<section class="about" role="img" aria-label="Small bowls of tapas with skewers">
  <svg class="abs" style="left:0;top:0" width="1200" height="537" viewBox="0 0 1200 537">
    <defs>
      <linearGradient id="aboutPanel" x1="0" y1="0" x2="0" y2="1">
        <stop offset="0" stop-color="#c4358f"/><stop offset="1" stop-color="#8c2094"/>
      </linearGradient>
    </defs>
    <path d="M650 0 Q560 268 650 537 L1200 537 L1200 0 Z" fill="url(#aboutPanel)"/>
  </svg>
  <h2>ABOUT CORK DEN</h2>
  <p>t is a long established fact that a reader will be distracted by the readable content of a page when looking at its layout. The point of using Lorem Ipsum is that it has a more-or-less normal distribution of letters, as opposed to using 'Content here, content here', making it look like readable English.</p>
  <a class="btn btn-more">READ MORE</a>
</section>

<section class="gallery-band"><h2>OUR GALLERY</h2></section>
<div class="tile" style="left:0;background:radial-gradient(ellipse at 45% 55%,#c0603a,#7a4b2a 55%,#3e2a1a)" role="img" aria-label="Bruschetta canapés on a board"></div>
<div class="tile" style="left:300px;background:radial-gradient(ellipse at 45% 60%,#8a1f22,#5a1612 55%,#a0582a)" role="img" aria-label="Red wine pouring into a glass"></div>
<div class="tile" style="left:600px;background:radial-gradient(ellipse at 50% 65%,#8a5232,#4a3326 55%,#2a2220)" role="img" aria-label="Skewered tapas on a slate"></div>
<div class="tile" style="left:900px;background:radial-gradient(ellipse at 45% 40%,#7a2326,#3e1d1a 60%,#8a8278)" role="img" aria-label="Two glasses of red wine at a table"></div>

<section class="reserve" role="img" aria-label="Dimly lit spread of tapas dishes">
  <h2>RESERVATIONS</h2>
  <p>t is a long established fact that a reader will be distracted by the readable content of a page when looking at its layout. The point of using Lorem Ipsum is that it has a more-or-less normal distribution</p>
  <a class="btn btn-book">BOOK NOW</a>
  <h3>OPENING HOURS</h3>
  <div class="hours">Thursday to Sunday 11am to Midnight</div>
</section>

<section class="map" role="img" aria-label="Street map of the park around Elder Colonial Lodge"></section>

<footer class="footer">
  <div class="col" style="left:131px">
    <h4>QUICK LINKS</h4>
    <ul><li>Home</li><li>About us</li><li>Food</li><li>Drink</li></ul>
  </div>
  <div class="col" style="left:320px">
    <h4>RESOURCES</h4>
    <ul><li>Map</li><li>Reservations</li><li>Elder Colonial lodge</li><li>Contact us</li></ul>
  </div>
  <div class="col" style="left:517px">
    <h4>OUR LOCTION</h4>
    <ul><li>Elder Colonial Lodge</li><li>Wendlow Reserve</li><li>Wendlow NSW 2163</li><li>555.010.2468</li><li>info@corkdenhaven.example</li></ul>
  </div>
  <div class="col" style="left:775px">
    <h4>GET SPECIAL OFFERS</h4>
  </div>
  <div class="offer-form"><span>Email address</span><b>Submit</b></div>
  <div class="footer-rule"></div>
  <div class="copyright">© 2018 Company Name  All right reserved</div>
</footer>

</body>
</html>
```